Packaging design for Virgin Coconut Oil. 100% pure cold pressed coconut oil

We need a new packaging and label design for our Virgin Coconut Oil product. It is currently marketed in the Philippines as a food supplement. We would like to try marketing it to other Asian countries such as Singapore, Malaysia and Hong Kong. The company has been producing this product since 2004 but now would like to venture into exporting our products overseas.

Would like to see designs with earth, natural "organic" colors. Fresh, Clean and pure look. Our trade mark is "Kestrel Meadow". Its a 100% pure cold pressed virgin coconut oil. All in all, we want to totally repackage our product and re-design the trademark to cater to export markets. Thanks!

Mid to High

Health Product

cadf82
9bcb3b
33b8a4
ffffff
3176b5
3276b5
0592cd
fbed22
fece3e

• Bottle shape design ideas.

```html
<!DOCTYPE html>
<html lang="en">
<head>
<meta charset="utf-8">
<title>Kestrel Meadow Coconut Oil Label</title>
<link rel="stylesheet" href="https://fonts.googleapis.com/css2?family=Raleway:wght@200;400&family=Quicksand:wght@400&display=swap">
<style>
  :root {
    --backdrop: #e9e9e9;
    --label-top: #8db20a;
    --label-bottom: #6b991b;
    --label-ink: #ffffff;
    --drop-tint: #6a9410;
  }
  html, body {
    margin: 0;
    padding: 0;
    width: 1200px;
    height: 1200px;
    overflow: hidden;
    background: var(--backdrop);
  }
  .label {
    display: block;
    width: 1200px;
    height: 1200px;
  }
  .brand-primary {
    font-family: "Raleway", sans-serif;
    font-weight: 400;
    font-size: 190px;
    fill: var(--label-ink);
  }
  .brand-secondary {
    font-family: "Raleway", sans-serif;
    font-weight: 200;
    font-size: 135px;
    fill: var(--label-ink);
  }
  .product-name {
    font-family: "Quicksand", sans-serif;
    font-size: 46px;
    fill: var(--label-ink);
  }
  .product-claim {
    font-family: "Quicksand", sans-serif;
    font-size: 30px;
    fill: var(--label-ink);
  }
  .label-ring {
    fill: none;
    stroke: var(--label-ink);
    stroke-width: 1.5;
  }
  .oil-drop {
    fill: var(--drop-tint);
    opacity: 0.55;
  }
</style>
</head>
<body>
<svg class="label" viewBox="0 0 1200 1200" xmlns="http://www.w3.org/2000/svg">
  <defs>
    <linearGradient id="label-fill" x1="0" y1="0" x2="0" y2="1">
      <stop offset="0" stop-color="var(--label-top)"/>
      <stop offset="1" stop-color="var(--label-bottom)"/>
    </linearGradient>
  </defs>
  <circle cx="600" cy="600" r="450" fill="url(#label-fill)"/>
  <circle class="label-ring" cx="600" cy="600" r="434"/>
  <text class="brand-primary" x="908" y="571" text-anchor="end">Kestrel</text>
  <text class="brand-secondary" x="908" y="743" text-anchor="end">Meadow</text>
  <path class="oil-drop" d="M600 801 C585 830 556 855 556 882 A44 44 0 0 0 644 882 C644 855 615 830 600 801 Z"/>
  <text class="product-name" x="600" y="947" text-anchor="middle">Coconut Oil</text>
  <text class="product-claim" x="600" y="992" text-anchor="middle">100% pure</text>
</svg>
</body>
</html>
```